Business Card Design for CoreLeafHarmony

We need the new logo on a business card for 3 employees:
Norma Kepple, PhD, Advanced Instructor and Practitioner of PulseWeave Vitalis Practice (email: norma@coreleafharmony.example)
Ted Halloran, Business Manager (email: ted@coreleafharmony.example)
Rosa Pilgrew, Administrative Assistant (email: rosa@quillgrove.example)

Target Market(s)

healthcare professionals

Industry/Entity Type

Alternative Medicine

Contact Information for Business Card

Names, titles, emails (names, titles, emails are in project description), phone, address, website, with logo and tagline. See below for address, phone, website: 418 Fennick St, Bldg 12, Ste 307
Linden Cove, CA 95999
831-555-0174
www.coreleafharmony.example
Tagline: Craft of Balance, Light of Renewal

Font styles to use
Other font styles liked:
• Gabriela

Colors
00a990
86cfc6
6b449b
b7a5cd
85abd2
abd036

Requirements
Must have
• Colors and style that match the logo design - shades such as blue, green, purple
• Compatible or same font as in the logo
Nice to have
• Nice if it goes with the theme of Norma's last business card - uploaded below
Should not have
• colors or style in conflict with the logo

```html
<!DOCTYPE html>
<html lang="en">
<head>
<meta charset="utf-8">
<title>CoreLeafHarmony Business Card</title>
<link href="https://fonts.googleapis.com/css2?family=Gabriela&family=Montserrat:wght@400;500&display=swap" rel="stylesheet">
<style>
  :root {
    --stage: #2b2b2b;
    --purple: #4a2a78;
    --purple-deep: #3d2266;
    --white: #ffffff;
    --ink: #3a3a3a;
    --grey: #5a5a5a;
    --blue: #1c73bd;
    --teal: #00a990;
    --mark-faint: #eef2f3;
  }
  * { margin: 0; padding: 0; box-sizing: border-box; }
  html, body { width: 1200px; height: 738px; overflow: hidden; }
  body {
    background: var(--stage);
    position: relative;
    font-family: "Montserrat", Arial, sans-serif;
  }
  .card {
    position: absolute;
    top: 226px;
    width: 500px;
    height: 286px;
    overflow: hidden;
    box-shadow: 0 10px 30px rgba(0,0,0,0.45);
  }
  .card--back { left: 70px; background: var(--purple); }
  .back-brand {
    position: absolute;
    left: 0; right: 0; top: 92px;
    display: flex; align-items: center; justify-content: center; gap: 18px;
  }
  .back-brand__dot {
    width: 70px; height: 70px; border-radius: 50%;
    background: var(--white);
  }
  .back-brand__name {
    font-family: "Gabriela", Georgia, serif;
    font-size: 34px;
    color: var(--white);
  }
  .back-web {
    position: absolute; left: 0; right: 0; bottom: 40px;
    text-align: center;
    font-size: 11px; letter-spacing: 0.5px;
    color: var(--white);
  }
  .card--front { left: 630px; background: var(--white); }
  .front-decor {
    position: absolute; left: 26px; top: 50px;
    width: 210px; height: 210px; border-radius: 50%;
    background: var(--mark-faint);
  }
  .front-brand {
    position: absolute; right: 26px; top: 26px;
    display: flex; align-items: center; gap: 10px;
  }
  .front-brand__dot {
    width: 48px; height: 48px; border-radius: 50%;
    background: var(--teal);
  }
  .front-brand__name {
    font-family: "Gabriela", Georgia, serif;
    font-size: 20px;
    color: var(--purple-deep);
  }
  .person { position: absolute; left: 44px; top: 160px; }
  .person__name {
    font-family: "Gabriela", Georgia, serif;
    font-size: 24px; color: var(--blue);
    line-height: 1.1; font-weight: 400;
  }
  .person__title { font-size: 12px; color: var(--grey); margin-top: 2px; }
  .contact {
    position: absolute; left: 44px; top: 214px;
    list-style: none; font-size: 12px; color: var(--ink);
  }
  .contact li { display: flex; align-items: center; gap: 8px; line-height: 18px; }
  .contact svg { width: 9px; height: 9px; fill: var(--blue); flex: none; }
  .address {
    position: absolute; right: 30px; top: 168px;
    text-align: right; font-size: 12px; line-height: 17px; color: var(--ink);
    font-style: normal;
  }
</style>
</head>
<body>
  <section class="card card--back" aria-label="Card back">
    <div class="back-brand">
      <span class="back-brand__dot"></span>
      <span class="back-brand__name">CoreLeafHarmony</span>
    </div>
    <p class="back-web">www.coreleafharmony.example</p>
  </section>

  <section class="card card--front" aria-label="Card front">
    <div class="front-decor"></div>
    <div class="front-brand">
      <span class="front-brand__dot"></span>
      <span class="front-brand__name">CoreLeafHarmony</span>
    </div>
    <div class="person">
      <h1 class="person__name">Rosa Pilgrew</h1>
      <p class="person__title">Administrative Assistant</p>
    </div>
    <ul class="contact">
      <li><svg viewBox="0 0 10 10" aria-hidden="true"><path d="M2 0h2l1 2.5-1.3 1a6 6 0 0 0 2.8 2.8l1-1.3L10 6v2a2 2 0 0 1-2 2A8 8 0 0 1 0 2a2 2 0 0 1 2-2z"/></svg>831-555-0174</li>
      <li><svg viewBox="0 0 10 10" aria-hidden="true"><path d="M0 2h10v6H0z M0 2l5 3.5L10 2" fill="none" stroke="#1c73bd" stroke-width="1.2"/></svg>rosa@quillgrove.example</li>
      <li><svg viewBox="0 0 10 10" aria-hidden="true"><circle cx="5" cy="5" r="4.3" fill="none" stroke="#1c73bd" stroke-width="1.2"/><path d="M1 5h8M5 1c-2 2.5-2 5.5 0 8M5 1c2 2.5 2 5.5 0 8" fill="none" stroke="#1c73bd" stroke-width="0.9"/></svg>www.coreleafharmony.example</li>
    </ul>
    <address class="address">
      418 Fennick St,<br>
      Bldg 12, Ste 307<br>
      Linden Cove, CA 95999
    </address>
  </section>
</body>
</html>
```